Local fast-growing company in the service sector

We are looking for a modern business card design, which should also appear on our letterheads

Target Market(s)

Private and industrial sectors

Contact Information for Business Card

Vorname Name
Lindkofer Str. 18
71468 Remsfeld
Tel.: 07163-418259-0
Name@kovaltec-pbz.de

Colors
9d9d9d
919191
aaaaaa

Requirements
Must have
• The logo (file) in silver

```html
<!DOCTYPE html>
<html lang="de">
<head>
<meta charset="utf-8">
<title>Kovaltec – Visitenkarte</title>
<link rel="stylesheet" href="https://fonts.googleapis.com/css2?family=Quicksand:wght@500;700&display=swap">
<style>
  :root {
    --backdrop: #e4e4e4;
    --card: #ffffff;
    --silver-dark: #919191;
    --silver: #9d9d9d;
    --silver-light: #aaaaaa;
    --ink: #6f6f6f;
    --faint: #f1f1f1;
  }
  html, body {
    margin: 0;
    width: 1200px;
    height: 1000px;
    overflow: hidden;
    background: var(--backdrop);
    font-family: "Quicksand", sans-serif;
  }
  .business-card {
    position: absolute;
    left: 160px;
    top: 260px;
    width: 880px;
    height: 480px;
    background: var(--card);
    border-radius: 28px;
    box-shadow: 0 10px 30px rgba(0,0,0,0.12);
    overflow: hidden;
  }
  .brand {
    position: absolute;
    left: 70px;
    top: 80px;
    display: flex;
    align-items: center;
    gap: 24px;
  }
  .brand-mark {
    width: 64px;
    height: 64px;
    background: var(--silver-light);
  }
  .brand-name {
    font-size: 66px;
    font-weight: 700;
    color: var(--silver);
    letter-spacing: 2px;
    line-height: 1;
  }
  .decor-panel {
    position: absolute;
    right: 70px;
    top: 60px;
    width: 230px;
    height: 200px;
    background: var(--faint);
    border-radius: 6px;
  }
  .contact {
    position: absolute;
    left: 70px;
    top: 232px;
    margin: 0;
    padding: 0;
    list-style: none;
  }
  .contact-item {
    display: flex;
    align-items: center;
    gap: 20px;
    height: 47px;
    font-size: 26px;
    font-weight: 500;
    color: var(--silver-dark);
  }
  .contact-item--name {
    font-size: 30px;
    font-weight: 700;
    color: var(--silver);
    height: 56px;
  }
  .contact-icon {
    width: 24px;
    height: 24px;
    fill: var(--ink);
    flex: none;
  }
</style>
</head>
<body>
  <section class="business-card">
    <div class="brand">
      <div class="brand-mark"></div>
      <div class="brand-name">KOVALTEC</div>
    </div>
    <div class="decor-panel" role="img" aria-label="Großes, dezentes Markenzeichen als Dekoration"></div>
    <ul class="contact">
      <li class="contact-item contact-item--name">
        <svg class="contact-icon" viewBox="0 0 24 24"><path d="M6 4 L20 12 L6 20 Z"/></svg>
        <span>Vorname Name</span>
      </li>
      <li class="contact-item">
        <svg class="contact-icon" viewBox="0 0 24 24"><path d="M2 9 C2 4 22 4 22 9 L22 11 L17 11 L17 8 L7 8 L7 11 L2 11 Z M5 13 L19 13 L21 20 L3 20 Z"/></svg>
        <span>07163-418259-0</span>
      </li>
      <li class="contact-item">
        <svg class="contact-icon" viewBox="0 0 24 24"><path d="M2 5 L22 5 L12 13 Z M2 7.5 L12 15.5 L22 7.5 L22 19 L2 19 Z"/></svg>
        <span>Name@kovaltec-pbz.de</span>
      </li>
      <li class="contact-item">
        <svg class="contact-icon" viewBox="0 0 24 24"><path d="M12 3 L23 12 L20 12 L20 21 L14 21 L14 15 L10 15 L10 21 L4 21 L4 12 L1 12 Z"/></svg>
        <span>Lindkofer Str. 18 71468 Remsfeld</span>
      </li>
    </ul>
  </section>
</body>
</html>
```